New business card design to go with our new logo

just want an eye-catching business card to go with our new logo. We are open to double sided or single sided. Just want it to have the following info on it. Whatever layout you think looks best.

First and Last Name
Title
Phone 801-555-7392
Address 214 W. Cedar Lane Pleasant Grove UT 84062
Email thecrew@marloweskennelandtreat.example

```html
<!DOCTYPE html>
<html lang="en">
<head>
<meta charset="utf-8">
<title>Marlowe's Kennel &amp; Treat – Business Card</title>
<link href="https://fonts.googleapis.com/css2?family=Lato:wght@400;700&display=swap" rel="stylesheet">
<style>
  :root {
    --backdrop: #2b2d31;
    --card: #ffffff;
    --orange: #f58a4b;
    --blue: #2fa6dc;
    --ink: #1e1e1e;
    --rule: #e3e3e3;
    --watermark: #ededed;
  }
  * { box-sizing: border-box; margin: 0; padding: 0; }
  html, body { width: 1200px; height: 864px; overflow: hidden; }
  body {
    background: var(--backdrop);
    font-family: "Lato", Arial, sans-serif;
    position: relative;
  }
  .card {
    position: absolute;
    width: 540px;
    height: 309px;
    background: var(--card);
    box-shadow: 0 10px 24px rgba(0,0,0,.45);
    overflow: hidden;
  }

  /* Back side */
  .card--back { left: 200px; top: 90px; }
  .watermark {
    position: absolute; inset: 0;
    display: flex; flex-direction: column; justify-content: space-evenly;
    padding: 0 10px;
  }
  .watermark-row {
    font-weight: 700; font-size: 36px; line-height: 44px;
    color: var(--watermark); text-align: center; white-space: nowrap;
    padding-bottom: 14px;
    border-bottom: 2px solid var(--watermark);
  }
  .watermark-row:last-child { border-bottom: none; padding-bottom: 0; }
  .back-mark {
    position: absolute; left: 50%; top: 50%;
    width: 180px; height: 180px; margin: -90px 0 0 -90px;
    border-radius: 50%;
    background: var(--blue);
  }

  /* Front side */
  .card--front { left: 230px; top: 470px; }
  .brand {
    position: absolute; top: 20px; left: 0; right: 0;
    display: flex; flex-direction: column; align-items: center; gap: 12px;
  }
  .brand-dot {
    width: 84px; height: 84px; border-radius: 50%;
    background: var(--blue);
  }
  .brand-name {
    font-weight: 700; font-size: 26px; color: var(--orange);
    letter-spacing: .3px;
  }
  .divider {
    position: absolute; left: 36px; right: 36px; top: 176px;
    border-top: 1px solid var(--rule);
  }
  .person {
    position: absolute; left: 36px; top: 186px;
    font-size: 15px; line-height: 19px; color: var(--ink);
  }
  .person-name { font-weight: 700; font-size: 17px; color: var(--orange); letter-spacing: .5px; }
  .person-title { color: var(--blue); }
  .contact {
    position: absolute; right: 30px; top: 232px;
    list-style: none; text-align: right;
    font-size: 14px; line-height: 21px; color: var(--ink);
  }
  .contact li { display: flex; justify-content: flex-end; align-items: center; gap: 8px; }
  .contact svg { width: 12px; height: 12px; fill: var(--blue); flex: none; }
</style>
</head>
<body>

  <section class="card card--back" aria-label="Card back">
    <div class="watermark" aria-hidden="true">
      <div class="watermark-row">Marlowe's Kennel &amp; Treat</div>
      <div class="watermark-row">Marlowe's Kennel &amp; Treat</div>
      <div class="watermark-row">Marlowe's Kennel &amp; Treat</div>
    </div>
    <div class="back-mark"></div>
  </section>

  <section class="card card--front" aria-label="Card front">
    <div class="brand">
      <div class="brand-dot"></div>
      <div class="brand-name">Marlowe's Kennel &amp; Treat</div>
    </div>
    <div class="divider"></div>

    <div class="person">
      <div class="person-name">DANA WHITLEY</div>
      <div class="person-title">Managing Director</div>
      <div class="person-address">214 W. Cedar Lane<br>Pleasant Grove UT 84062</div>
    </div>

    <ul class="contact">
      <li>801-555-7392
        <svg viewBox="0 0 24 24" aria-hidden="true"><path d="M6.6 10.8a15.1 15.1 0 0 0 6.6 6.6l2.2-2.2a1 1 0 0 1 1-.25 11.4 11.4 0 0 0 3.6.57 1 1 0 0 1 1 1V20a1 1 0 0 1-1 1A17 17 0 0 1 3 4a1 1 0 0 1 1-1h3.5a1 1 0 0 1 1 1c0 1.25.2 2.45.57 3.6a1 1 0 0 1-.25 1z"/></svg>
      </li>
      <li>thecrew@marloweskennelandtreat.example
        <svg viewBox="0 0 24 24" aria-hidden="true"><path d="M2 5h20v14H2z M3.5 6.5 12 13l8.5-6.5" fill="none" stroke="#2fa6dc" stroke-width="2"/></svg>
      </li>
      <li>www.marloweskennelandtreat.example
        <svg viewBox="0 0 24 24" aria-hidden="true"><circle cx="12" cy="12" r="10"/><path d="M2 12h20M12 2c3 3 3 17 0 20M12 2c-3 3-3 17 0 20" fill="none" stroke="#fff" stroke-width="1.5"/></svg>
      </li>
    </ul>
  </section>

</body>
</html>
```